Business Card for Restaurant Vendal

This project consist of creating 2 design for business card of restaurant named Vendal.

The attached specs below are 'ONLY SUGGESTION' if you have others ideas. You are welcome to post it.

1) Restaurant Card

Adresse:
2784 Côte du Pinard Vert
Montréal (Qc) H4K 3T8

Website:
www.ven-dal.ca

Phone:
438-719-2046

2) Employee Card

Name: Lorna Pik
Title: Owner

Address:
2784 Côte du Pinard Vert
Montréal (Qc) H4K 3T8

Email:lorna@ven-dal.ca
Phone Number:438-719-2046
Cellphone Number:514-830-4162

 The attached specs are 'ONLY SUGGESTION' if you have others ideas.  You are welcome to post it.

Industry/Entity Type

Restaurant

Requirements
Must have
• UV Card Spot

To print Spot UV business cards you would have to submit 2 files for each side. The first file "base" would be your regular design file as it would have been in any other case. The 2nd file "UV mask" is a black/white file. The BLACK color will indicate the areas that will be covered with the UV high gloss finish. To upload the files, please combine front design and front mask file in one P
Nice to have
• 1) The font of the logo should be ink effect
2) black background with wallpaper effect
3) The specs below are 'ONLY SUGGESTION' if you have others ideas. You are welcome to post it.

```html
<!DOCTYPE html>
<html lang="fr">
<head>
<meta charset="utf-8">
<title>Vendal – Business Cards</title>
<link rel="stylesheet" href="https://fonts.googleapis.com/css2?family=Open+Sans:wght@400;600;700&display=swap">
<style>
  :root {
    --backdrop: #3a3a3a;
    --card-black: #161616;
    --card-white: #ffffff;
    --lantern-red: #d0201f;
    --pattern-tone: #242424;
    --ink: #111111;
    --text-grey: #b9b9b9;
  }
  * { margin: 0; padding: 0; box-sizing: border-box; }
  html, body { width: 1200px; height: 716px; overflow: hidden; }
  body {
    background: var(--backdrop);
    font-family: "Open Sans", Arial, sans-serif;
    position: relative;
  }
  .card {
    position: absolute;
    top: 210px;
    width: 520px;
    height: 297px;
    border-radius: 4px;
    box-shadow: 0 10px 30px rgba(0,0,0,.45);
    overflow: hidden;
  }
  .card-back { left: 50px; background: var(--card-black); }
  .card-front { left: 630px; background: var(--card-white); }

  .lantern-pattern {
    position: absolute;
    left: 190px; top: 0;
    width: 330px; height: 297px;
    background: radial-gradient(circle at 60% 50%, #2c2c2c, var(--pattern-tone) 70%);
  }
  .lantern-feature {
    position: absolute;
    left: 250px; top: 62px;
    width: 130px; height: 124px;
    border-radius: 50%;
    background: var(--lantern-red);
  }
  .contact-list {
    position: absolute;
    left: 26px; bottom: 40px;
    list-style: none;
    color: var(--text-grey);
    font-size: 12px;
    line-height: 17px;
  }
  .contact-list li { display: flex; align-items: flex-start; }
  .contact-list .icon {
    width: 14px; height: 17px;
    margin-right: 12px;
    flex-shrink: 0;
    display: flex; align-items: center; justify-content: center;
  }
  .contact-list .icon svg { width: 10px; height: 10px; fill: var(--lantern-red); }

  .brand {
    position: absolute;
    left: 0; right: 0; top: 78px;
    display: flex; align-items: center; justify-content: center;
    gap: 18px;
  }
  .brand-name {
    font-size: 76px;
    font-weight: 700;
    color: var(--ink);
    letter-spacing: 1px;
    line-height: 1;
  }
  .brand-dot {
    width: 34px; height: 34px;
    border-radius: 50%;
    background: var(--lantern-red);
  }
  .tagline {
    position: absolute;
    left: 0; right: 0; top: 182px;
    text-align: center;
    font-size: 15px;
    font-weight: 600;
    color: var(--ink);
  }
</style>
</head>
<body>

<section class="card card-back">
  <div class="lantern-pattern" role="img" aria-label="Spot UV pattern of paper lanterns on black"></div>
  <div class="lantern-feature" role="img" aria-label="Red foil paper lantern illustration"></div>
  <ul class="contact-list">
    <li>
      <span class="icon"><svg viewBox="0 0 10 10"><path d="M5 0a3.5 3.5 0 0 0-3.5 3.5C1.5 6 5 10 5 10s3.5-4 3.5-6.5A3.5 3.5 0 0 0 5 0zm0 5a1.5 1.5 0 1 1 0-3 1.5 1.5 0 0 1 0 3z"/></svg></span>
      <span>2784 Côte du Pinard Vert<br>Montréal (Qc) H4K 3T8</span>
    </li>
    <li>
      <span class="icon"><svg viewBox="0 0 10 10"><circle cx="5" cy="5" r="5"/></svg></span>
      <span>438-719-2046</span>
    </li>
    <li>
      <span class="icon"><svg viewBox="0 0 10 10"><rect x="2.5" y="0" width="5" height="10" rx="1"/></svg></span>
      <span>514-830-4162</span>
    </li>
    <li>
      <span class="icon"><svg viewBox="0 0 10 10"><rect x="0" y="1.5" width="10" height="7" rx="1"/></svg></span>
      <span>lorna@ven-dal.ca</span>
    </li>
    <li>
      <span class="icon"><svg viewBox="0 0 10 10"><circle cx="5" cy="5" r="5"/></svg></span>
      <span>www.ven-dal.ca</span>
    </li>
  </ul>
</section>

<section class="card card-front">
  <div class="brand">
    <span class="brand-name">Vendal</span>
    <span class="brand-dot"></span>
  </div>
  <p class="tagline">Resto-Bar Japonais · Izakaya · 居酒屋</p>
</section>

</body>
</html>
```